Der Designer hat mir ein super Logo entworfen sehr schnell tolle Zusammenarbeit. Ist nur zu empfehlen
Zielgruppe
Es handelt sich um eine Haus und Immobilienverwaltung die Zielgruppe sind Eigentümer der Häuser und Firmen
Aufgabenstellung
Edel klassisch

```html
<!DOCTYPE html>
<html lang="de">
<head>
<meta charset="utf-8">
<title>Velmar – Visitenkarten</title>
<link href="https://fonts.googleapis.com/css2?family=Arimo:wght@400&display=swap" rel="stylesheet">
<style>
  :root {
    --stage: #4d4d4d;
    --card-light: #ffffff;
    --card-dark: #343434;
    --brand-blue: #79b0cc;
    --brand-green: #86a998;
    --brand-grey: #b3b3b3;
    --text: #555555;
    --name: #7a7a72;
    --rule: #d4d4d4;
  }
  * { margin: 0; padding: 0; box-sizing: border-box; }
  html, body { width: 1200px; height: 1200px; overflow: hidden; }
  body {
    background: var(--stage);
    font-family: "Arimo", Arial, sans-serif;
    position: relative;
  }
  .card {
    position: absolute;
    width: 467px;
    height: 302px;
    box-shadow: 4px 4px 8px rgba(0,0,0,0.45);
    overflow: hidden;
  }
  .card--front-light { left: 68px; top: 238px; background: var(--card-light); }
  .card--front-dark { left: 641px; top: 238px; background: var(--card-dark); }
  .card--back-left { left: 68px; top: 710px; background: var(--card-light); }
  .card--back-right { left: 641px; top: 710px; background: var(--card-light); }

  .wordmark {
    position: absolute;
    left: 0; right: 0; top: 118px;
    text-align: center;
    font-size: 52px;
    letter-spacing: 6px;
    color: var(--brand-grey);
    line-height: 1;
  }

  .divider {
    position: absolute;
    left: 191px; top: 22px;
    width: 1px; height: 226px;
    background: var(--rule);
  }
  .person {
    position: absolute;
    left: 0; width: 191px; top: 114px;
    text-align: center;
  }
  .person__name { font-size: 21px; color: var(--name); line-height: 1; white-space: nowrap; }
  .person__role { font-size: 11.5px; color: var(--name); margin-top: 8px; }

  .wordmark--small {
    position: absolute;
    right: 27px; top: 84px;
    font-size: 24px;
    letter-spacing: 3px;
    color: var(--brand-grey);
    line-height: 1;
  }

  .address {
    position: absolute;
    right: 27px; top: 146px;
    font-size: 12.5px;
    color: var(--text);
    white-space: nowrap;
  }
  .contact {
    position: absolute;
    left: 234px; right: 27px; top: 170px;
    font-size: 12.5px;
  }
  .contact__heading {
    text-align: right;
    color: var(--brand-green);
    font-size: 13px;
    margin-bottom: 7px;
  }
  .contact__row {
    display: flex;
    justify-content: space-between;
    gap: 10px;
    height: 21px;
    align-items: center;
    white-space: nowrap;
  }
  .contact__label { color: var(--brand-blue); }
  .contact__value { color: var(--text); }

  .band {
    position: absolute;
    left: 0; right: 0; top: 263px;
    height: 12px;
    display: flex;
  }
  .band__grey { width: 80px; background: var(--brand-grey); }
  .band__green { flex: 1; background: var(--brand-green); }
</style>
</head>
<body>

  <section class="card card--front-light">
    <div class="wordmark">VELMAR</div>
  </section>

  <section class="card card--front-dark">
    <div class="wordmark">VELMAR</div>
  </section>

  <section class="card card--back-left">
    <div class="person">
      <div class="person__name">Jana Velbrück</div>
      <div class="person__role">Geschäftsführung</div>
    </div>
    <div class="divider"></div>
    <div class="wordmark--small">VELMAR</div>
    <div class="address">Lindenhofweg 12 | 10115 Berlin</div>
    <div class="contact">
      <div class="contact__heading">Kontakt</div>
      <div class="contact__row"><span class="contact__label">Telefon:</span><span class="contact__value">+49 030 555 01 247</span></div>
      <div class="contact__row"><span class="contact__label">Telefax:</span><span class="contact__value">+49 030 555 01 247</span></div>
      <div class="contact__row"><span class="contact__label">E-Mail:</span><span class="contact__value">Velbrueck@Velmar.de</span></div>
    </div>
    <div class="band"><div class="band__grey"></div><div class="band__green"></div></div>
  </section>

  <section class="card card--back-right">
    <div class="person">
      <div class="person__name">Sabine Hollmer</div>
      <div class="person__role">Geschäftsführung</div>
    </div>
    <div class="divider"></div>
    <div class="wordmark--small">VELMAR</div>
    <div class="address">Lindenhofweg 12 | 10115 Berlin</div>
    <div class="contact">
      <div class="contact__heading">Kontakt</div>
      <div class="contact__row"><span class="contact__label">Telefon:</span><span class="contact__value">+49 030 555 01 247</span></div>
      <div class="contact__row"><span class="contact__label">Telefax:</span><span class="contact__value">+49 030 555 01 247</span></div>
      <div class="contact__row"><span class="contact__label">E-Mail:</span><span class="contact__value">Hollmer@Velmar.de</span></div>
    </div>
    <div class="band"><div class="band__grey"></div><div class="band__green"></div></div>
  </section>

</body>
</html>
```